innovative investment real estate sales firm

We are a uniquely collabrative firm that seeks to bring a conultative approach to uncovering hidden opportunities for our clients, our website needs to convey our client focused approach. Our firm specializes in the sale of apartment properties in Southern California. We have a team of researchers, transaction coordinators and marketing personal to support our geographically specialized advisers. We need a website that introduces clients to our unique way of better helping them achieve their investment goals.

Target Market(s)

High net worth individuals and families

Industry/Entity Type

Real Estate Agent

Font styles to use
Other font styles liked:
• please use font provided

Requirements
Must have
• Stories of our recent projects
• Features on our people
• email capture for viewing inventory
• content that showcases our unique consultative approach that uncovers unrealized opportunities

```html
<!DOCTYPE html>
<html lang="en">
<head>
<meta charset="utf-8">
<title>Meridian Advisers — Multifamily Properties</title>
<link href="https://fonts.googleapis.com/css2?family=Montserrat:wght@400;500;600;700&family=Open+Sans:wght@400;600&display=swap" rel="stylesheet">
<style>
:root{
  --teal:#17a3bd;
  --teal-dark:#0f8aa1;
  --lime:#8dc63f;
  --ink:#2b2f33;
  --text:#555b60;
  --muted:#8a9095;
  --paper:#ffffff;
  --mist:#ececec;
  --night:#1d2023;
  --bar:#3a3f44;
}
*{box-sizing:border-box;margin:0;padding:0}
html,body{width:1200px;height:2946px;overflow:hidden}
body{position:relative;background:var(--paper);font-family:"Open Sans",Arial,sans-serif;color:var(--text)}
.abs{position:absolute}

/* hero */
.hero-photo{left:0;top:0;width:1200px;height:652px;background:linear-gradient(180deg,#5a86c6 0%,#93b3dc 35%,#b9895e 60%,#6e7a4a 85%,#4e5a36 100%)}
.header{left:122px;top:0;width:954px;height:206px;background:var(--paper);box-shadow:0 6px 18px rgba(0,0,0,.25)}
.topbar{left:0;top:0;width:954px;height:55px;border-bottom:1px solid #e3e3e3;font-family:"Montserrat",sans-serif;color:var(--ink)}
.topbar .label{left:15px;top:21px;font-weight:700;font-size:10px;white-space:nowrap}
.topbar .signup{left:147px;top:13px;width:202px;height:30px;border:1.5px solid var(--teal);border-radius:15px;font-size:10.5px;padding:7px 0 0 16px}
.topbar .signup span{position:absolute;right:0;top:-1.5px;width:34px;height:30px;border-radius:0 15px 15px 0;border:1.5px solid var(--teal)}
.topbar .signup span::after{content:"";position:absolute;left:12px;top:9px;border-left:7px solid var(--teal);border-top:5px solid transparent;border-bottom:5px solid transparent}
.topbar .phone{left:520px;top:17px;font-size:16px;font-weight:500;display:flex;align-items:center;gap:8px;white-space:nowrap}
.topbar .mail{left:664px;top:21px;font-size:10.5px;display:flex;align-items:center;gap:7px;white-space:nowrap}
.social{display:flex;gap:6px}
.social i{display:block;width:22px;height:22px;border-radius:50%;background:var(--teal)}
.topbar .social{left:860px;top:16px}
.brand{display:flex;align-items:center;gap:12px}
.brand .mark{width:46px;height:46px;background:var(--teal)}
.brand .name{font-family:"Montserrat",sans-serif;font-weight:700;font-size:20px;color:var(--teal-dark);letter-spacing:1px;white-space:nowrap}
.header .brand{left:22px;top:96px}
.nav{right:14px;top:141px;display:flex;gap:18px;font-family:"Montserrat",sans-serif;font-size:11px;font-weight:600;color:var(--ink);white-space:nowrap}
.nav a{text-decoration:none;color:inherit;padding-bottom:10px}
.nav a.active{border-bottom:2px solid var(--teal)}
.slider-arrows{left:122px;top:566px;display:flex;gap:4px}
.slider-arrows b{width:32px;height:32px;background:var(--teal);display:flex;align-items:center;justify-content:center}
.callout{left:742px;top:255px;width:324px;height:348px;background:var(--teal);padding:14px 14px 0;color:#fff}
.callout .kicker{font-size:12px;font-weight:600;font-family:"Montserrat",sans-serif}
.callout .title{font-size:15px;font-weight:700;font-family:"Montserrat",sans-serif;margin-top:2px;white-space:nowrap}
.callout .photo{margin-top:10px;width:290px;height:140px;background:linear-gradient(135deg,#f1e6d6,#c9b59b 60%,#8b9aa8)}
.callout p{font-size:11px;line-height:16px;margin-top:14px}
.btn-lime{display:inline-block;background:var(--lime);color:#fff;border-radius:16px;font-family:"Montserrat",sans-serif;font-weight:700;font-size:10px;padding:10px 22px}
.callout .btn-lime{margin-top:14px}

/* projects */
.section-title{left:0;width:1200px;text-align:center;font-family:"Montserrat",sans-serif;font-weight:700;color:var(--ink)}
.projects-title{top:710px;font-size:19px;display:flex;justify-content:center;align-items:center;gap:18px}
.projects-title::before,.projects-title::after{content:"";width:84px;height:2px;background:var(--lime)}
.projects-lead{top:742px;left:0;width:1200px;text-align:center;font-size:12px}
.card{top:800px;width:216px;height:382px;background:#fff;box-shadow:0 2px 8px rgba(0,0,0,.22);padding:7px 8px}
.card .photo{height:178px}
.card h3{font-family:"Montserrat",sans-serif;font-size:13px;font-weight:700;color:var(--lime);margin-top:20px}
.card .where{font-size:10px;color:var(--ink);font-weight:600;white-space:nowrap}
.card p{font-size:11.5px;line-height:16px;margin-top:8px}
.card .stat{display:block;margin-top:18px;background:var(--teal);border-radius:16px;color:#fff;font-family:"Montserrat",sans-serif;font-size:11px;font-weight:700;text-align:center;padding:9px 0}
.skyline-light{left:0;top:1208px;width:1200px;height:173px;background:linear-gradient(180deg,#ffffff 0%,#e4e6e8 55%,#cfd3d6 100%)}
.load-more{top:1240px;left:0;width:1200px;text-align:center;font-family:"Montserrat",sans-serif;font-size:10px;font-weight:600;color:var(--ink)}

/* email capture */
.capture{left:0;top:1381px;width:1200px;height:290px;background:linear-gradient(180deg,#22272c 0%,#2d3c4a 55%,#3a4a52 100%)}
.capture h2{top:82px;left:0;width:1200px;text-align:center;font-family:"Montserrat",sans-serif;font-size:18px;color:var(--lime);font-weight:700}
.capture p{top:108px;left:0;width:1200px;text-align:center;font-size:11.5px;color:#fff;font-weight:600}
.capture .field{left:285px;top:145px;width:473px;height:61px;border:2px solid var(--teal);border-radius:30px;background:rgba(0,0,0,.45);color:#ddd;font-size:11px;padding:22px 0 0 28px}
.capture .submit{left:770px;top:145px;width:143px;height:61px;border-radius:30px;background:var(--teal);color:#fff;font-family:"Montserrat",sans-serif;font-weight:700;font-size:19px;text-align:center;line-height:61px}

/* team */
.team{left:0;top:1671px;width:1200px;height:706px;background:var(--mist)}
.team .eyebrow{top:92px;font-size:10px}
.team .title{top:108px;font-size:19px;color:var(--teal)}
.team .lead{top:154px;left:118px;width:964px;text-align:center;font-size:12px;line-height:19px}
.member{top:270px;width:200px;text-align:center;font-family:"Montserrat",sans-serif}
.member .avatar{width:176px;height:176px;border-radius:50%;margin:0 auto;border:5px solid #fff;background:linear-gradient(180deg,#c9cdd2,#8e98a4);box-shadow:0 1px 4px rgba(0,0,0,.15)}
.member.current .avatar{border-color:var(--lime)}
.member h4{margin-top:16px;font-size:13px;color:var(--ink);font-weight:600}
.member span{font-size:9px;font-weight:700;color:var(--ink)}
.team .arrow{top:340px}
.roles{top:594px;left:245px;display:flex;gap:8px}
.roles b{height:40px;border-radius:20px;background:var(--teal);color:#fff;font-family:"Montserrat",sans-serif;font-size:12px;font-weight:700;display:flex;align-items:center;justify-content:center}

/* footer */
.skyline-dark{left:0;top:2377px;width:1200px;height:58px;background:linear-gradient(180deg,var(--mist) 0%,#5b5f63 45%,#1e2124 100%)}
.footer{left:0;top:2435px;width:1200px;height:442px;background:linear-gradient(180deg,#1d2023,#2a2e32)}
.footer .brand{left:120px;top:108px}
.footer .brand .mark{width:40px;height:40px;background:#fff}
.footer .brand .name{color:#fff;font-size:18px}
.footer .about{left:120px;top:178px;width:290px;font-size:11.5px;line-height:21px;color:#fff}
.footer .about a{color:var(--lime);text-decoration:none;font-weight:600}
.footer .contact{left:120px;top:278px;font-size:11.5px;color:#fff;line-height:20px}
.footer .contact .row{display:flex;gap:10px;align-items:flex-start;margin-bottom:6px}
.footer .contact .big{color:var(--lime);font-size:16px;font-weight:600;font-family:"Montserrat",sans-serif}
.footer h5{font-family:"Montserrat",sans-serif;font-size:14px;color:#fff;font-weight:600}
.news{left:462px;top:112px;width:340px}
.news-item{display:flex;gap:12px;margin-top:14px}
.news-item .thumb{width:92px;height:82px;flex:none}
.news-item h6{font-family:"Montserrat",sans-serif;font-size:11px;color:var(--lime);font-weight:600;line-height:15px}
.news-item .meta{font-size:9px;color:#aaa;margin-top:4px}
.news-item p{font-size:10px;color:#fff;line-height:14px;margin-top:4px}
.news-item p a{color:var(--lime);text-decoration:none}
.news .more{display:inline-block;margin-top:12px;background:var(--teal);color:#fff;font-size:9px;font-weight:700;font-family:"Montserrat",sans-serif;border-radius:16px;padding:10px 16px}
.links{left:862px;top:112px}
.links ul{list-style:none;margin-top:10px}
.links li{font-size:11px;color:var(--teal);line-height:32px}
.copybar{left:0;top:2877px;width:1200px;height:69px;background:var(--bar)}
.copybar .note{left:120px;top:28px;font-size:10px;color:#fff}
.copybar .note b{color:var(--lime);font-weight:600}
.copybar .social{left:996px;top:23px}
.copybar .social i{background:#fff}
</style>
</head>
<body>

<div class="abs hero-photo" role="img" aria-label="Photo of a row of multi-storey apartment townhomes with cypress trees under a blue sky"></div>

<header class="abs header">
  <div class="abs topbar">
    <div class="abs label">AVAILABLE PROPERTIES</div>
    <div class="abs signup">Enter Email Address<span></span></div>
    <div class="abs phone">
      <svg width="16" height="14" viewBox="0 0 16 14"><path d="M3 1l3 3-2 2c1 2 3 4 5 5l2-2 3 3-2 2C6 13 1 8 1 3z" fill="#8dc63f"/></svg>555.010.4827</div>
    <div class="abs mail">
      <svg width="14" height="10" viewBox="0 0 14 10"><rect width="14" height="10" fill="#8dc63f"/><path d="M0 0l7 5 7-5" stroke="#fff" fill="none"/></svg>email@meridianadv.example</div>
    <div class="abs social"><i></i><i></i><i></i></div>
  </div>
  <div class="abs brand"><span class="mark"></span><span class="name">MERIDIAN ADVISERS</span></div>
  <nav class="abs nav">
    <a class="active">HOME</a><a>ABOUT US</a><a>SERVICES</a><a>PROPERTIES</a><a>RECENT PROJECTS</a><a>OUR TEAM</a><a>NEWS</a><a>CONTACT</a>
  </nav>
</header>

<div class="abs slider-arrows">
  <b><svg width="14" height="12" viewBox="0 0 14 12"><path d="M7 1L2 6l5 5M12 1L7 6l5 5" stroke="#fff" stroke-width="2" fill="none"/></svg></b>
  <b><svg width="14" height="12" viewBox="0 0 14 12"><path d="M2 1l5 5-5 5M7 1l5 5-5 5" stroke="#fff" stroke-width="2" fill="none"/></svg></b>
</div>

<aside class="abs callout">
  <div class="kicker">Uncover Unrealized Opportunities through our</div>
  <div class="title">UNIQUE CONSULTATIVE APPROACH</div>
  <div class="photo" role="img" aria-label="Photo of an adviser reviewing documents with a client couple"></div>
  <p>We are a uniquely collaborative firm that seeks to bring a consultative approach to uncovering hidden opportunities in achieving your investment goals.</p>
  <span class="btn-lime">KNOW MORE ▸</span>
</aside>

<h2 class="abs section-title projects-title">RECENT PROJECTS</h2>
<p class="abs projects-lead">Lorem ipsum dolor sit amet, consectetur adipiscing elit. Sed nec turpis dignissim, condimentum lectus eu, vulputate justo.</p>

<article class="abs card" style="left:122px">
  <div class="photo" role="img" aria-label="Photo of an apartment courtyard with landscaped gardens" style="background:linear-gradient(180deg,#9fc3e6,#7e9a5a 60%,#b8a98a)"></div>
  <h3>LOREM IPSUM</h3><div class="where">Atlantic Boulevard | Los Angeles County</div>
  <p>Lorem ipsum dolor sit amet, consectetur adipiscing elit. Sed nec turpis dignissim, condimentum lectus eu, vulputate justo.</p>
  <span class="stat">268 Units | $ 29,800.00</span>
</article>
<article class="abs card" style="left:369px">
  <div class="photo" role="img" aria-label="Photo of brick-and-siding townhouse apartments" style="background:linear-gradient(180deg,#c5d6e8,#a48a6c 55%,#6f6a5c)"></div>
  <h3>LOREM IPSUM</h3><div class="where">Sunset Boulevard | Los Angeles County</div>
  <p>Lorem ipsum dolor sit amet, consectetur adipiscing elit. Sed nec turpis dignissim, condimentum lectus eu, vulputate justo.</p>
  <span class="stat">120 Units | $ 36,000.00</span>
</article>
<article class="abs card" style="left:617px">
  <div class="photo" role="img" aria-label="Photo of an apartment complex with a swimming pool" style="background:linear-gradient(180deg,#86b6e0,#c8a77a 50%,#3fb5cf)"></div>
  <h3>LOREM IPSUM</h3><div class="where">Cedarwood Ave | Orange County</div>
  <p>Lorem ipsum dolor sit amet, consectetur adipiscing elit. Sed nec turpis dignissim, condimentum lectus eu, vulputate justo.</p>
  <span class="stat">223 Units | $ 25,500.00</span>
</article>
<article class="abs card" style="left:864px">
  <div class="photo" role="img" aria-label="Photo of a Mediterranean-style apartment building with palm trees" style="background:linear-gradient(180deg,#7fb2e3,#d9b88e 55%,#8aa26a)"></div>
  <h3>LOREM IPSUM</h3><div class="where">Victory Boulevard | Los Angeles County</div>
  <p>Lorem ipsum dolor sit amet, consectetur adipiscing elit. Sed nec turpis dignissim, condimentum lectus eu, vulputate justo.</p>
  <span class="stat">200 Units | $ 27,800.00</span>
</article>

<div class="abs skyline-light" role="img" aria-label="Faded city skyline illustration"></div>
<div class="abs load-more">LOAD MORE<br>▾</div>

<section class="abs capture" role="img" aria-label="Night photo of a coastal city harbor behind the email sign-up">
  <h2 class="abs">WANT TO SEE AVAILABLE PROPERTIES IN SOUTHERN CALIFORNIA?</h2>
  <p class="abs">Lorem ipsum dolor sit amet, consectetur adipiscing elit. Sed nec turpis dignissim, condimentum lectus eu, vulputate justo. Proin venenatis in sapien in luctus.</p>
  <div class="abs field">Enter Your Email Address</div>
  <div class="abs submit">SUBMIT</div>
</section>

<section class="abs team">
  <div class="abs section-title eyebrow">OUR TEAM</div>
  <h2 class="abs section-title title">PEOPLE WHO MAKE IT HAPPEN</h2>
  <p class="abs lead">Lorem ipsum dolor sit amet, consectetur adipiscing elit. Sed nec turpis dignissim, condimentum lectus eu, vulputate justo. Proin venenatis in sapien in luctus. Nullam pulvinar tortor vitae leo ultricies lobortis. Interdum et malesuada fames ac ante ipsum primis in faucibus. Morbi vel risus ac felis elementum egestas ultrices eu neque. Etiam varius tristique leo, quis convallis nisl.</p>
  <svg class="abs arrow" style="left:118px" width="22" height="40" viewBox="0 0 22 40"><path d="M20 2L3 20l17 18" stroke="#c4c4c4" stroke-width="2" fill="none"/></svg>
  <svg class="abs arrow" style="left:1060px" width="22" height="40" viewBox="0 0 22 40"><path d="M2 2l17 18L2 38" stroke="#c4c4c4" stroke-width="2" fill="none"/></svg>
  <div class="abs member current" style="left:179px"><div class="avatar" role="img" aria-label="Portrait photo of the CEO"></div><h4>DANIEL BROOKS</h4><span>CEO &amp; FOUNDER</span></div>
  <div class="abs member" style="left:403px"><div class="avatar" role="img" aria-label="Portrait photo of the director"></div><h4>OWEN CARTER</h4><span>DIRECTOR</span></div>
  <div class="abs member" style="left:611px"><div class="avatar" role="img" aria-label="Portrait photo of the assistant director"></div><h4>LAURA BENNETT</h4><span>ASSISTANT DIRECTOR</span></div>
  <div class="abs member" style="left:819px"><div class="avatar" role="img" aria-label="Portrait photo of the marketing head"></div><h4>ETHAN WALSH</h4><span>MARKETING HEAD</span></div>
  <div class="abs roles">
    <b style="width:132px">ADVISERS</b><b style="width:163px">RESEARCHERS</b><b style="width:257px">TRANSACTION COORDINATORS</b><b style="width:134px">MARKETING</b>
  </div>
</section>

<div class="abs skyline-dark" role="img" aria-label="Dark city skyline silhouette"></div>

<footer class="abs footer">
  <div class="abs brand"><span class="mark"></span><span class="name">MERIDIAN ADVISERS</span></div>
  <p class="abs about">Lorem ipsum dolor sit amet, consectetur adipiscing elit. Sed nec turpis dignissim, condimentum lectus eu. Proin venenatis in sapien in luctus. Nullam pulvinar tortor vitae leo ultricies lobortis. <a>About Us ▸</a></p>
  <div class="abs contact">
    <div class="row"><svg width="12" height="16" viewBox="0 0 12 16"><path d="M6 0a6 6 0 016 6c0 4-6 10-6 10S0 10 0 6a6 6 0 016-6z" fill="#8dc63f"/><circle cx="6" cy="6" r="2" fill="#1d2023"/></svg><span>240 Harbor Row<br>Bayview, CA 90000</span></div>
    <div class="row"><svg width="14" height="14" viewBox="0 0 16 14"><path d="M3 1l3 3-2 2c1 2 3 4 5 5l2-2 3 3-2 2C6 13 1 8 1 3z" fill="#8dc63f"/></svg><span class="big">555.010.4827</span></div>
    <div class="row"><svg width="14" height="10" viewBox="0 0 14 10" style="margin-top:5px"><rect width="14" height="10" fill="#8dc63f"/><path d="M0 0l7 5 7-5" stroke="#1d2023" fill="none"/></svg><span>email@meridianadv.example</span></div>
  </div>
  <div class="abs news">
    <h5>Recent News</h5>
    <div class="news-item">
      <div class="thumb" role="img" aria-label="Photo of an apartment pool" style="background:linear-gradient(180deg,#86b6e0,#3fb5cf)"></div>
      <div><h6>Lorem ipsum dolor sit amet, consectetur adipiscing elit.</h6><div class="meta">June 27th, 2017 | 0 Comments</div><p>Sed nec turpis dignissim, condimentum lectus eu, vulputate justo. Proin venenatis in sapien in luctus. <a>More</a></p></div>
    </div>
    <div class="news-item">
      <div class="thumb" role="img" aria-label="Photo of townhouse apartments" style="background:linear-gradient(180deg,#c5d6e8,#8a7a66)"></div>
      <div><h6>Lorem ipsum dolor sit amet, consectetur adipiscing elit.</h6><div class="meta">June 27th, 2017 | 0 Comments</div><p>Sed nec turpis dignissim, condimentum lectus eu, vulputate justo. Proin venenatis in sapien in luctus. <a>More</a></p></div>
    </div>
    <span class="more">MORE NEWS</span>
  </div>
  <div class="abs links">
    <h5>Quick Links</h5>
    <ul><li>Home</li><li>About Us</li><li>Services</li><li>Properties</li><li>Recent Projects</li><li>Our Team</li><li>News</li><li>Contact</li></ul>
  </div>
</footer>

<div class="abs copybar">
  <div class="abs note">© 2017 <b>Meridian Advisers</b>. All Rights Reserved</div>
  <div class="abs social"><i></i><i></i><i></i></div>
</div>

</body>
</html>
```